Letterhead

We have a new logo and would like to design electronic letterhead with our new logo. We have two office locations. One of our offices is moving in July.

```html
<!DOCTYPE html>
<html lang="en">
<head>
<meta charset="utf-8">
<title>Holt Attorneys at Law — Letterhead</title>
<link rel="stylesheet" href="https://fonts.googleapis.com/css2?family=Open+Sans:wght@400;600;700&family=Arimo:wght@700&display=swap">
<style>
  :root {
    --backdrop: #e4e5e5;
    --paper: #ffffff;
    --ink-navy: #262838;
    --brand-blue: #2a68b4;
    --heading-navy: #1c2766;
    --body-grey: #4a4a4a;
    --footer-ink: #2f2f2f;
  }
  * { box-sizing: border-box; margin: 0; padding: 0; }
  html, body {
    width: 1200px; height: 945px; overflow: hidden;
    background: var(--backdrop);
  }
  .canvas { position: relative; width: 1200px; height: 945px; }
  .letterhead {
    position: absolute; left: 282px; top: 22px;
    width: 636px; height: 900px;
    background: var(--paper);
    box-shadow: 0 2px 14px rgba(0,0,0,0.12);
    font-family: "Open Sans", sans-serif;
    color: var(--body-grey);
    overflow: hidden;
  }
  .edge-band-dark {
    position: absolute; left: 0; top: 0; width: 10px; height: 650px;
    background: var(--ink-navy);
  }
  .edge-band-blue {
    position: absolute; left: 0; top: 650px; width: 14px; bottom: 0;
    background: var(--brand-blue);
  }
  .brand {
    position: absolute; left: 50px; top: 48px;
    display: flex; align-items: center; gap: 10px;
  }
  .brand-mark {
    width: 18px; height: 18px; background: var(--ink-navy);
  }
  .brand-name {
    font-family: "Open Sans", sans-serif;
    font-weight: 600; font-size: 24px; line-height: 1;
    color: var(--ink-navy);
  }
  .salutation {
    position: absolute; left: 58px; top: 190px;
    font-family: "Arimo", sans-serif; font-weight: 700;
    font-size: 16px; color: var(--heading-navy);
  }
  .letter-body {
    position: absolute; left: 80px; top: 222px; width: 500px;
    font-size: 13px; line-height: 17px; text-align: justify;
  }
  .letter-body p { margin-bottom: 18px; }
  .signature {
    position: absolute; left: 120px; top: 515px; width: 170px; height: 60px;
    background: linear-gradient(90deg, #f1f1f1, #e6e6e6);
    border-radius: 4px;
  }
  .contact {
    position: absolute; left: 70px; bottom: 36px;
    font-size: 12.5px; line-height: 17px; color: var(--footer-ink);
  }
  .contact-line { display: flex; align-items: center; gap: 6px; }
  .contact-line svg { width: 11px; height: 11px; fill: var(--brand-blue); }
  .postal { margin-top: 4px; }
  .website {
    position: absolute; right: 38px; bottom: 150px;
    font-size: 12.5px; color: var(--brand-blue);
  }
  .website strong { font-weight: 700; }
</style>
</head>
<body>
<div class="canvas">
  <article class="letterhead">
    <div class="edge-band-dark"></div>
    <div class="edge-band-blue"></div>

    <header class="brand">
      <span class="brand-mark" aria-hidden="true"></span>
      <span class="brand-name">Holt Attorneys at Law</span>
    </header>

    <h1 class="salutation">Dear Mr. Ellis,</h1>

    <section class="letter-body">
      <p>Lorem Ipsum is simply dummy text of the printing and typesetting industry. Lorem Ipsum has been the industry's standard dummy text ever since the 1500s, when an unknown printer took a galley of type and scrambled it to make a type specimen book. It has survived not only five centuries, but also the leap into electronic typesetting, remaining essentially unchanged.</p>
      <p>The standard chunk of Lorem Ipsum used since the 1500s is reproduced below for those interested. Sections 1.10.32 and 1.10.33 from "de Finibus Bonorum et Malorum" by Cicero are also reproduced in their exact original form, accompanied by English versions from the 1914 translation by H. Rackham</p>
      <p>Lorem Ipsum is simply dummy text of the printing and typesetting industry. Lorem Ipsum has been the industry's standard dummy text ever since the 1500s, when an unknown printer took a galley of type and scrambled it to make a type specimen book. It has survived not only five centuries, but also the leap into electronic typesetting, remaining essentially unchanged. It was popularised in the</p>
    </section>

    <div class="signature" role="img" aria-label="Handwritten signature of the sender"></div>

    <div class="website">www.<strong>holtlegal</strong>.com</div>

    <footer class="contact">
      <div class="contact-line">
        <svg viewBox="0 0 12 12" aria-hidden="true"><path d="M1 4c0-2 2-3 5-3s5 1 5 3l-1 1-2-1V3H4v1L2 5 1 4zm2 2h6l1 5H2l1-5zm3 1.2a1.6 1.6 0 1 0 0 3.2 1.6 1.6 0 0 0 0-3.2z"/></svg>
        <span>+61 7 555 0148</span>
      </div>
      <div class="contact-line">
        <svg viewBox="0 0 12 12" aria-hidden="true"><path d="M1 3h10v7H1V3zm1 1v.4l4 2.6 4-2.6V4H2z"/></svg>
        <span>info@holtlegal.com</span>
      </div>
      <div class="postal">Po. box 201, Street Name,<br>City Name, Zip Code - 00000</div>
    </footer>
  </article>
</div>
</body>
</html>
```